Larkfield Institute Logo & Business card

Larkfield Institute - Professional ICT Training
business is a training center.
Logo and business card that have an ID.
bold publicity, distinct, and prestige image
"Ensure professional Success"
that will attract target customer to come and take a look. that will look prestige on certificate after graduation, that will serve as a business tool to attract Business and enterprise customer (let them send their staff for training)
Updates

upgrade to with logo vector design

Target Market(s)

young professionals, university students, youth building career in IT fields

Industry/Entity Type

Education

Contact Information for Business Card

Address
Phone
email
Socialia

Font styles to use
Sans Serif

Colors

Designer to choose colors to be used in the design.

Requirements
Must have
• Logo Identity
• uniqueness
Nice to have
• catch phrase or illustration
Should not have
• just use alphabet as logo.

```html
<!DOCTYPE html>
<html lang="en">
<head>
<meta charset="utf-8">
<title>Larkfield Institute – Business Card</title>
<link href="https://fonts.googleapis.com/css2?family=Open+Sans:wght@400;500;600&display=swap" rel="stylesheet">
<style>
  :root {
    --page-bg: #eceef1;
    --card-white: #ffffff;
    --card-grey: #e9eaee;
    --brand-purple: #4a2a86;
    --brand-violet: #7a2a95;
    --brand-blue: #1f73b7;
    --brand-cyan: #2a9fd6;
    --text-dark: #1c1c1c;
    --ribbon-light: #d9d6dc;
  }
  * { box-sizing: border-box; margin: 0; padding: 0; }
  html, body {
    width: 1200px; height: 900px; overflow: hidden;
    background: var(--page-bg);
    font-family: "Open Sans", Arial, sans-serif;
  }
  .business-card {
    position: absolute; left: 100px; top: 160px;
    width: 1000px; height: 580px;
    border-radius: 34px; overflow: hidden;
    background: linear-gradient(135deg, var(--card-grey) 0%, var(--card-white) 45%, var(--card-grey) 100%);
    box-shadow: 0 18px 40px rgba(0,0,0,0.12);
  }
  .brand-mark {
    position: absolute; left: 90px; top: 40px;
    width: 190px; height: 190px; border-radius: 50%;
    background: radial-gradient(circle at 35% 30%, #8fd3ef 0%, var(--brand-cyan) 45%, var(--brand-blue) 100%);
  }
  .brand-name {
    position: absolute; left: 318px; top: 70px;
    font-size: 50px; font-weight: 500; letter-spacing: -0.5px;
    color: var(--brand-purple); white-space: nowrap;
  }
  .brand-tagline {
    position: absolute; left: 321px; top: 142px;
    font-size: 21px; font-weight: 500; letter-spacing: 3.4px;
    color: var(--brand-blue); white-space: nowrap;
  }
  .contact-list { position: absolute; left: 60px; top: 262px; list-style: none; }
  .contact-item {
    display: flex; align-items: flex-start; gap: 18px;
    height: 48px; font-size: 23px; line-height: 30px; color: var(--text-dark);
  }
  .contact-item--address { line-height: 30px; }
  .contact-icon { flex: 0 0 32px; width: 32px; height: 32px; }
  .holder { position: absolute; right: 70px; top: 240px; text-align: right; }
  .holder-name { font-size: 24px; font-weight: 600; color: var(--brand-blue); }
  .holder-role { font-size: 17px; color: var(--text-dark); margin-top: 6px; }
  .social {
    position: absolute; right: 60px; top: 428px;
    display: flex; align-items: center; gap: 8px;
    font-size: 16px; font-weight: 500; color: var(--brand-blue);
  }
  .social-square { width: 22px; height: 22px; border-radius: 4px; background: var(--brand-blue); }
  .card-waves { position: absolute; left: 0; top: 0; width: 1000px; height: 580px; }
</style>
</head>
<body>
  <div class="business-card">
    <svg class="card-waves" viewBox="0 0 1000 580" aria-hidden="true">
      <defs>
        <linearGradient id="ribbonPurple" x1="0" y1="0" x2="1" y2="0">
          <stop offset="0" stop-color="#2f9fd3"/>
          <stop offset="0.45" stop-color="#7a2a95"/>
          <stop offset="1" stop-color="#4a2a86"/>
        </linearGradient>
        <linearGradient id="ribbonBlue" x1="0" y1="0" x2="1" y2="0">
          <stop offset="0" stop-color="#1f73b7"/>
          <stop offset="0.6" stop-color="#2a9fd6"/>
          <stop offset="1" stop-color="#7a2a95"/>
        </linearGradient>
      </defs>
      <path d="M0 520 C 180 470, 380 470, 560 500 C 700 522, 820 500, 1000 470 L1000 580 L0 580 Z" fill="#f4f4f6"/>
      <path d="M0 500 C 200 450, 420 455, 600 488 L 600 500 C 420 472, 200 470, 0 528 Z" fill="url(#ribbonBlue)"/>
      <path d="M460 480 C 640 470, 820 420, 1000 300 L1000 330 C 820 450, 640 500, 460 492 Z" fill="url(#ribbonPurple)"/>
      <path d="M560 470 C 690 420, 840 380, 1000 350 L1000 372 C 840 400, 700 440, 600 490 Z" fill="var(--ribbon-light)"/>
      <path d="M640 420 C 760 380, 880 360, 1000 340 L1000 350 C 880 370, 760 392, 660 430 Z" fill="#2a9fd6"/>
    </svg>

    <div class="brand-mark" role="img" aria-label="Larkfield Institute brand emblem"></div>
    <div class="brand-name">Larkfield Institute</div>
    <div class="brand-tagline">PROFESSIONAL ICT TRAINING</div>

    <ul class="contact-list">
      <li class="contact-item">
        <svg class="contact-icon" viewBox="0 0 32 32" aria-hidden="true"><circle cx="16" cy="16" r="16" fill="var(--brand-blue)"/><path d="M11 8 l3 0 l1.5 4 l-2 1.5 a10 10 0 0 0 5 5 l1.5 -2 l4 1.5 l0 3 a2 2 0 0 1 -2 2 A14 14 0 0 1 9 10 a2 2 0 0 1 2 -2 Z" fill="#fff"/></svg>
        <span>0861 27 34 19</span>
      </li>
      <li class="contact-item">
        <svg class="contact-icon" viewBox="0 0 32 32" aria-hidden="true"><circle cx="16" cy="16" r="16" fill="var(--brand-blue)"/><rect x="8" y="10.5" width="16" height="11" rx="1.5" fill="#fff"/><path d="M8.5 11.5 L16 17 L23.5 11.5" fill="none" stroke="var(--brand-blue)" stroke-width="1.5"/></svg>
        <span>info@larkfieldinstitute.com</span>
      </li>
      <li class="contact-item">
        <svg class="contact-icon" viewBox="0 0 32 32" aria-hidden="true"><circle cx="16" cy="16" r="16" fill="var(--brand-blue)"/><g fill="none" stroke="#fff" stroke-width="1.5"><circle cx="16" cy="16" r="8"/><ellipse cx="16" cy="16" rx="3.5" ry="8"/><path d="M8 16 H24 M9.5 12 H22.5 M9.5 20 H22.5"/></g></svg>
        <span>www.larkfieldinstitute.com</span>
      </li>
      <li class="contact-item contact-item--address">
        <svg class="contact-icon" viewBox="0 0 32 32" aria-hidden="true"><circle cx="16" cy="16" r="16" fill="var(--brand-blue)"/><path d="M16 7 a6 6 0 0 1 6 6 c0 4.5 -6 12 -6 12 s-6 -7.5 -6 -12 a6 6 0 0 1 6 -6 Z" fill="#fff"/><circle cx="16" cy="13" r="2.3" fill="var(--brand-blue)"/></svg>
        <span>No. 2176, birch lane<br>fairview 482</span>
      </li>
    </ul>

    <div class="holder">
      <div class="holder-name">Dana Whitfield</div>
      <div class="holder-role">Manager</div>
    </div>

    <div class="social">
      <span class="social-square"></span>
      <span>Socialia</span>
    </div>
  </div>
</body>
</html>
```